Label designs for three different cider varieties

The Larkmoor Perry Works is a family run business. We have been making cider within the family as a hobby for over 100 years and we have recently decided to start to try to sell the cider. Therefore this project is to create a logo and three product labels for three different varieties of cider. So we should end up with four files; one for the logo and one for each of the labels. The files need to be in an editable format for us so that we can add edit the batch numbers e.g. PNG file.
For the logo we would like to use the Pellow Family Shield since Pellow is our family name. We would like it adapted into a cider themed crest, for example with apples and trees. We are open to ideas about the logo but this is just our initial idea. Example of the original Pellow Family Shield can be seen in the link below:
http://www.vinshadeheraldry.net/arms/Pellow-England.jpg
The labels should be no bigger than 93mm in height and 213mm in length. Each label should be similar in style so it is clear the three different varieties of cider are from the same company. Each label must have the following information since this is a legal requirement:
- The logo you have created
- The Larkmoor Perry Works Ltd.
- 52 Mirefield Row, Taunton, Somerset, TA4 9QX
- Alcohol: 6% vol
- 500ml
- Allergens: Contains Sulphites for freshness
- There needs to be space on the label for batch numbers. This is four numbers e.g. 1701.
- Family craft cider makers using only premium apples from our own traditional Somerset orchard.
The names of the three cider varieties are:
- Larkmoor Heritage
- Larkmoor Amber
- Larkmoor Kingsbury
Our initial idea is that each variety would have its own colour associated with it; i.e. black themed label for Larkmoor Heritage, gold themed label for Larkmoor Amber and a red themed label for Larkmoor Kingsbury. The crest logo you have created would then be in the themed colour for that cider variety i.e. black, gold or red.
We would like the labels to reflect the following themes for our brand:
- High end premium brand
- Clean and simple design
- Modern
Overall we are very open to ideas and we do not want to constrain your creativity. All of the above is just our initial ideas but we would love to see what ideas you have. The only things that cannot change are what must be on the label since this is a legal requirement we have to meet.

```html
<!DOCTYPE html>
<html lang="en">
<head>
<meta charset="utf-8">
<title>Larkmoor Perry Works – Cider Labels</title>
<link rel="stylesheet" href="https://fonts.googleapis.com/css2?family=Great+Vibes&family=Petit+Formal+Script&family=Lato:wght@400&display=swap">
<style>
  :root {
    --sheet: #ffffff;
    --label-bg: #231f20;
    --label-edge: #5a5657;
    --ink: #ffffff;
    --batch-box: #ffffff;
    --batch-ink: #231f20;
    --amber: #b3a779;
    --kingsbury: #b0391d;
    --heritage: #c9d948;
  }
  * { margin: 0; padding: 0; box-sizing: border-box; }
  html, body {
    width: 914px; height: 1200px; overflow: hidden;
    background: var(--sheet);
  }
  .sheet { position: relative; width: 914px; height: 1200px; }
  .label {
    position: absolute; left: 4px; width: 910px; height: 387px;
    background: var(--label-bg);
    border: 1px solid var(--label-edge);
    color: var(--ink);
  }
  .label--amber { top: 3px; --theme: var(--amber); }
  .label--kingsbury { top: 406px; --theme: var(--kingsbury); }
  .label--heritage { top: 810px; --theme: var(--heritage); }

  .batch-box {
    position: absolute; left: 22px; top: 20px; width: 82px; height: 196px;
    background: var(--batch-box);
    color: var(--batch-ink);
    font: 9px/1 "Lato", sans-serif;
    text-align: center; padding-top: 8px;
  }
  .variety-name {
    position: absolute; left: 0; right: 0; top: 20px;
    text-align: center;
    font: 48px/1.1 "Great Vibes", cursive;
  }
  .volume {
    position: absolute; right: 70px; top: 22px; width: 90px;
    text-align: center;
    font: 14px/24px "Lato", sans-serif;
  }
  .crest-mark {
    position: absolute; left: 50%; top: 96px; transform: translateX(-50%);
    width: 130px; height: 170px;
    display: flex; flex-direction: column; align-items: center; justify-content: center; gap: 12px;
    color: var(--theme);
    font: 34px/1 "Great Vibes", cursive;
  }
  .crest-mark .dot {
    width: 70px; height: 70px; border-radius: 50%;
    background: var(--theme);
  }
  .company {
    position: absolute; left: 0; right: 0; top: 280px;
    text-align: center;
    font: 25px/1 "Great Vibes", cursive;
  }
  .tagline {
    position: absolute; left: 0; right: 0; top: 313px;
    text-align: center;
    font: 11px/20px "Petit Formal Script", cursive;
  }
  .allergens {
    position: absolute; left: 48px; top: 349px;
    font: 9px/1 "Lato", sans-serif;
  }
  .address {
    position: absolute; right: 28px; top: 287px; width: 110px;
    text-align: center; font-style: normal;
    font: 9px/22px "Lato", sans-serif;
  }
</style>
</head>
<body>
<main class="sheet">

  <section class="label label--amber">
    <div class="batch-box">Batch Number</div>
    <h1 class="variety-name">Larkmoor Amber</h1>
    <p class="volume">500ml<br>6% vol</p>
    <div class="crest-mark" role="img" aria-label="Pellow family crest in amber"><span class="dot"></span>Pellow</div>
    <p class="company">The Larkmoor Perry Works Ltd.</p>
    <p class="tagline">Family craft cider makers using only premium apples<br>from our own traditional Somerset orchard.</p>
    <p class="allergens">Contains Sulphites for freshness</p>
    <address class="address">52 Mirefield Row,<br>Taunton,<br>Somerset,<br>TA4 9QX</address>
  </section>

  <section class="label label--kingsbury">
    <div class="batch-box">Batch Number</div>
    <h1 class="variety-name">Larkmoor Kingsbury</h1>
    <p class="volume">500ml<br>6% vol</p>
    <div class="crest-mark" role="img" aria-label="Pellow family crest in red"><span class="dot"></span>Pellow</div>
    <p class="company">The Larkmoor Perry Works Ltd.</p>
    <p class="tagline">Family craft cider makers using only premium apples<br>from our own traditional Somerset orchard.</p>
    <p class="allergens">Contains Sulphites for freshness</p>
    <address class="address">52 Mirefield Row,<br>Taunton,<br>Somerset,<br>TA4 9QX</address>
  </section>

  <section class="label label--heritage">
    <div class="batch-box">Batch Number</div>
    <h1 class="variety-name">Larkmoor Heritage</h1>
    <p class="volume">500ml<br>6% vol</p>
    <div class="crest-mark" role="img" aria-label="Pellow family crest in apple green"><span class="dot"></span>Pellow</div>
    <p class="company">The Larkmoor Perry Works Ltd.</p>
    <p class="tagline">Family craft cider makers using only premium apples<br>from our own traditional Somerset orchard.</p>
    <p class="allergens">Contains Sulphites for freshness</p>
    <address class="address">52 Mirefield Row,<br>Taunton,<br>Somerset,<br>TA4 9QX</address>
  </section>

</main>
</body>
</html>
```